Business Card Design

We are a design build firm specializing in the construction and design of kitchens. We are a "green" company, hence the logo. Here are some IDEAS we came up with. I am asking to use this for every person in our firm, so I will need to be able to edit the text. On the back, I am thinking of a very simple design... maybe carry over the white band around the edge. Maybe a simple saying on the back "Renovating homes from Concept to Completion".

Please see our current website for our style and design info
www.cabinetrefitvalley.com (going to be forwarded to maplehearthllc.com)

Industry/Entity Type

Construction

Contact Information for Business Card

Maple Hearth Design & Construction
Dana Wickford - Chief Designer
418 Birchwood Lane
Alder Falls, CT 06999
203.555.0172 C
203.555.0149 O
www.maplehearthllc.com
mhcabinets@mailbox.example

```html
<!DOCTYPE html>
<html lang="en">
<head>
<meta charset="utf-8">
<title>Maple Hearth Design &amp; Construction – Business Card</title>
<link rel="stylesheet" href="https://fonts.googleapis.com/css2?family=Noto+Serif:wght@400;700&display=swap">
<style>
  :root {
    --stage: #ece9e4;
    --green-light: #93d51c;
    --green-mid: #6fb516;
    --green-dark: #2c6a0e;
    --ink: #1f1f1f;
    --white: #ffffff;
    --rule: #3c6b1d;
  }
  * { box-sizing: border-box; margin: 0; padding: 0; }
  html, body { width: 1200px; height: 1084px; overflow: hidden; }
  body {
    background: var(--stage);
    font-family: "Noto Serif", Georgia, serif;
    position: relative;
  }
  .card {
    position: absolute;
    top: 76px;
    width: 533px;
    height: 937px;
    box-shadow: 0 2px 10px rgba(0,0,0,0.25);
    overflow: hidden;
  }
  .card--front {
    left: 57px;
    background: linear-gradient(100deg, var(--green-light) 0%, var(--green-mid) 45%, var(--green-dark) 100%);
    color: var(--white);
  }
  .card--back {
    left: 617px;
    background: var(--white);
    color: var(--ink);
    border: 1px solid #d8d8d8;
  }
  .brand {
    position: absolute;
    left: 0; right: 0;
    text-align: center;
    font-family: "Noto Serif", Georgia, serif;
    font-weight: 700;
  }
  .brand__mark {
    display: block;
    width: 46px; height: 46px;
    border-radius: 50%;
    margin: 0 auto 18px;
    background: currentColor;
  }
  .brand__mark--green { background: var(--green-mid); }
  .brand__name {
    display: block;
    font-size: 44px;
    letter-spacing: 1px;
    line-height: 1.1;
  }
  .brand__rule {
    display: block;
    height: 2px;
    margin: 12px auto 10px;
    background: currentColor;
    opacity: 0.8;
  }
  .brand__tagline {
    display: block;
    font-size: 23px;
    letter-spacing: 3px;
  }
  .card--front .brand { top: 110px; color: var(--white); }
  .card--front .brand__rule { width: 440px; }
  .card--back .brand { top: 345px; color: var(--ink); }
  .card--back .brand__rule { width: 480px; background: var(--rule); }

  .person {
    position: absolute;
    top: 500px; left: 0; right: 0;
    text-align: center;
  }
  .person__name { font-size: 29px; font-weight: 700; line-height: 1.3; }
  .person__role { font-size: 23px; font-weight: 400; margin-top: 4px; }

  .contact {
    position: absolute;
    top: 632px; left: 0; right: 0;
    list-style: none;
    text-align: center;
    font-size: 23px;
    line-height: 37px;
  }
  .contact__item { display: flex; justify-content: center; align-items: center; gap: 10px; }
  .contact__icon { width: 20px; height: 20px; fill: var(--white); flex: none; }

  .address {
    position: absolute;
    top: 803px; left: 0; right: 0;
    text-align: center;
    font-style: normal;
    font-size: 23px;
    line-height: 35px;
  }

  .slogan {
    position: absolute;
    top: 600px; left: 0; right: 0;
    text-align: center;
    font-size: 35px;
    line-height: 48px;
    color: var(--ink);
  }
</style>
</head>
<body>

<section class="card card--front" aria-label="Business card front">
  <div class="brand">
    <span class="brand__mark" aria-hidden="true"></span>
    <span class="brand__name">MAPLE HEARTH</span>
    <span class="brand__rule" aria-hidden="true"></span>
    <span class="brand__tagline">DESIGN &amp; CONSTRUCTION</span>
  </div>

  <div class="person">
    <p class="person__name">Dana Wickford</p>
    <p class="person__role">Chief Designer</p>
  </div>

  <ul class="contact">
    <li class="contact__item">
      <svg class="contact__icon" viewBox="0 0 20 20" aria-hidden="true"><circle cx="10" cy="10" r="9" fill="none" stroke="#fff" stroke-width="1.6"/><path d="M6.5 5.5l2 0 1 2.5-1.3 1a6 6 0 0 0 3 3l1-1.3 2.5 1v2c-4.5.5-8.7-3.7-8.2-8.2z"/></svg>
      <span>203.555.0149</span>
    </li>
    <li class="contact__item">
      <svg class="contact__icon" viewBox="0 0 20 20" aria-hidden="true"><rect x="5" y="1" width="10" height="18" rx="1.5"/><rect x="6.5" y="3" width="7" height="10" fill="#5a9a14"/><circle cx="10" cy="16" r="1.2" fill="#5a9a14"/></svg>
      <span>203.555.0172</span>
    </li>
    <li class="contact__item">
      <svg class="contact__icon" viewBox="0 0 20 20" aria-hidden="true"><rect x="2" y="5" width="16" height="11" rx="1"/><path d="M2.5 5.5l7.5 6 7.5-6" fill="none" stroke="#5a9a14" stroke-width="1.4"/></svg>
      <span>mhcabinets@mailbox.example</span>
    </li>
    <li class="contact__item">
      <svg class="contact__icon" viewBox="0 0 20 20" aria-hidden="true"><circle cx="10" cy="10" r="8.5"/><g fill="none" stroke="#4a8a12" stroke-width="1.2"><ellipse cx="10" cy="10" rx="3.5" ry="8.5"/><path d="M1.5 10h17M3 6h14M3 14h14"/></g></svg>
      <span>www.maplehearthllc.com</span>
    </li>
  </ul>

  <address class="address">
    418 Birchwood Lane Alder Falls<br>CT 06999
  </address>
</section>

<section class="card card--back" aria-label="Business card back">
  <div class="brand">
    <span class="brand__mark brand__mark--green" aria-hidden="true"></span>
    <span class="brand__name">MAPLE HEARTH</span>
    <span class="brand__rule" aria-hidden="true"></span>
    <span class="brand__tagline">DESIGN &amp; CONSTRUCTION</span>
  </div>
  <p class="slogan">Renovating homes from<br>Concept to Completion</p>
</section>

</body>
</html>
```